Broschüre für Toben – Balgen – Kraftprobe
Zielgruppe
Wir bieten Rangel und Raufkurse für Kinder ab dem Vorschulalter bis zu weiterführenden Schulen. Die Broschüre erhalten Lehrer, Erzieher und Direktoren der Einrichtungen an denen die Kurse Angeboten werden.
Aufgabenstellung
Design sollte eher Schlicht und modern wirken und an der homepage
www.boden-lernwerk.de orientiert sein.
Infobroschüre zum Durchblättern, kein Folder. Seitenfolge wie auf der Powerpoint präsentation.

```html
<!DOCTYPE html>
<html lang="de">
<head>
<meta charset="utf-8">
<title>Toben – Balgen – Kraftprobe · Broschüre</title>
<link href="https://fonts.googleapis.com/css2?family=Open+Sans:ital,wght@0,400;0,600;0,700;1,400;1,700&display=swap" rel="stylesheet">
<style>
:root{
  --bg:#e6e6e8;
  --paper:#f8f8f8;
  --ink:#4a4a4a;
  --red:#d2262b;
  --grey-box:#dedede;
}
*{margin:0;padding:0;box-sizing:border-box}
html,body{width:1200px;height:3351px;overflow:hidden;background:var(--bg);font-family:"Open Sans",Arial,sans-serif;color:var(--ink)}
.spread{position:absolute;width:614px;height:320px;display:flex;box-shadow:0 10px 18px rgba(0,0,0,.12)}
.page{position:relative;width:307px;height:320px;background:var(--paper);overflow:hidden}
.page.left{border-right:1px solid #ddd}
.bar{position:absolute;background:var(--red);color:#fff;font-weight:700;font-size:8.5px;line-height:12px;padding:1px 5px;text-transform:uppercase;letter-spacing:.2px;white-space:nowrap}
.bar.small{font-size:6px;line-height:8px;padding:1px 4px;font-style:italic}
.para{position:absolute;font-size:5.6px;line-height:7.6px;text-align:justify}
.para.box{background:var(--grey-box);padding:3px 4px}
.para.red{color:var(--red);font-style:italic}
.photo{position:absolute}
.label{position:absolute;font-size:5.4px;font-weight:700;color:#333;text-transform:uppercase}
.label .tag{display:inline-block;background:var(--red);color:#fff;padding:0 3px;margin-bottom:2px;font-style:italic}
.checks{position:absolute;list-style:none;font-size:5.4px;line-height:7px;color:var(--red);font-style:italic}
.checks li{margin-bottom:5px;padding-left:7px;position:relative}
.checks li::before{content:"✓";position:absolute;left:0}
.course{position:absolute;font-size:5.6px;line-height:7.2px}
.course h3{color:var(--red);font-style:italic;font-size:9px;line-height:11px;font-weight:700}
.course b{display:block;font-size:5.4px;text-transform:uppercase}
.course .para{position:static;margin-top:6px}
.rule{position:absolute;height:2px;background:var(--red)}
.person{position:absolute;font-size:5.4px;line-height:7px}
.person strong{display:block;text-transform:uppercase;font-size:5.6px}
.person em{color:var(--red);display:block;margin-top:4px}
</style>
</head>
<body>

<section class="spread" style="left:139px;top:202px">
  <div class="page left">
    <div class="bar" style="left:46px;top:20px">Rangeln und Raufen ist eine Urform</div>
    <div class="bar" style="left:46px;top:34px">der kindlichen Bewegung</div>
    <p class="para" style="left:76px;top:78px;width:208px">In der heutigen Zeit scheint es Eltern und Erziehungspersonen schwer zu fallen, den richtigen Mittelweg für die Erziehung der nächsten Generation zu finden. Wenn Kinder zu viel Freiraum haben, tun sie oft genau das, was Erwachsene nicht erwarten: sie raufen, streiten und rebellieren. Doch ist es richtig, dieses Verhalten bedingungslos zu unterbinden? Schließlich sind es Verhaltensweisen, die Kinder gerade dann zeigen, wenn sie sich frei entfalten dürfen.</p>
    <p class="para" style="left:76px;top:182px;width:208px">Rangeln und Raufen liegt in der menschlichen Natur. Es ist eine Urform der kindlichen Bewegung. Streit ist ein soziales Phänomen, das überall existiert und nicht zu vermeiden ist. Wenn man von Menschen erwartet, dass sie Konflikte fair lösen, darf ihnen der Weg dorthin nicht verwehrt bleiben. Kinder, die sich frei erproben, entwickeln sich zu selbstständigen Menschen.</p>
  </div>
  <div class="page">
    <div class="photo" role="img" aria-label="Foto: zwei Jungen stehen sich Stirn an Stirn im Park gegenüber" style="left:26px;top:0;width:232px;height:160px;background:linear-gradient(135deg,#6f9a4c,#b9c89a 55%,#8aa0b8)"></div>
    <p class="para box" style="left:30px;top:188px;width:246px">Es ist unsere tiefe Überzeugung, dass unser Kampfsport diese kindlichen Eigenschaften in eine gesunde Richtung lenken kann. Kinder werden spielerisch und friedlich miteinander zu raufen lernen, was ihrer kindlichen Neugierde entspricht. Sie erforschen die Kräfte ihres Körpers und testen ihre Grenzen. Sie haben Spaß, dürfen austoben und müssen einstecken. All das in einem friedlichen Umfeld, das klare Regeln festlegt und die Kinder zu Respekt und Selbstdisziplin motiviert.</p>
  </div>
</section>

<section class="spread" style="left:437px;top:605px">
  <div class="page left">
    <div class="bar" style="left:46px;top:20px">Friedliches Rangeln und Raufen zur</div>
    <div class="bar" style="left:46px;top:34px">Entwicklungsförderung</div>
    <p class="para" style="left:76px;top:74px;width:210px">Sich fit fühlen, sich etwas zutrauen und ein gesundes Selbstbewusstsein entwickeln – das sind positive Effekte von sportlichen Angeboten für Kinder und Jugendliche. Gerade bei jungen Menschen sollte der Spaß an der Bewegung gefördert werden, was dazu beiträgt, Sport zu einem selbstverständlichen Teil ihres Lebens zu machen.</p>
    <p class="para" style="left:76px;top:124px;width:210px">Unser Konzept basiert auf einem modernen Kampfsport, der Brazilian Jiu Jitsu heißt und statt Schlägen und Tritten auf das Einsetzen des eigenen Körpergewichts setzt, um den Gegenüber am Boden zu kontrollieren. Rangeln und Raufen stellt die Urform der kindlichen Bewegung dar. Neben diesem Spieltrieb ein sicherer und friedvoller Rahmen gegeben wird, bietet sich eine der besten Voraussetzungen für eine optimale körperliche und geistige Entwicklung. In unserem Kurs wird nicht nur gerangelt, sondern die Kinder auch spielerisch die effektivste Form der Selbstverteidigung näher gebracht. Unser Kampfsporttraining lehrt keine gefährliche Gewalt, sondern Achtung vor dem Partner.</p>
    <p class="para box" style="left:72px;top:238px;width:218px">Gerade aufgeweckte und im Unterricht unruhige Kinder finden ihren Platz gerne auf der Matte, wo sie sich messen und ihren Überschuss an Energie loswerden dürfen. Die Kinder erhalten Anerkennung, die sie möglicherweise in anderen Bereichen nicht bekommen, und haben durch den Sport die Chance, über sich hinauszuwachsen.</p>
  </div>
  <div class="page">
    <p class="para" style="left:30px;top:20px;width:226px">Steigerung des Selbstbewusstseins. Zusammen mit verbalen Strategien zur Konfliktlösung kann bereits im Vorfeld verhindert werden, dass Kinder in eine Opferrolle hineingeraten.</p>
    <p class="para box" style="left:26px;top:52px;width:234px">Rangeln und friedliches Raufen wird in der modernen Erziehung bereits als bedeutendes pädagogisches Medium erkannt. An der Umsetzung scheitert es jedoch meistens, da Erzieher und Lehrer ohne eigene Kampfsporterfahrungen oder spezielle Ausbildung zu großen Respekt vor dieser Thematik haben. Im Gegensatz dazu findet man Kampfsporttrainer, die Freude daran haben, dieses Thema kindgerecht zu vermitteln. Auf Basis unserer Ausbildung zum Pädagogen kombiniert mit langjähriger Erfahrung als aktive Trainer sind unsere Programme für Kinder konzipiert.</p>
    <div class="label" style="left:30px;top:200px"><span class="tag">Toben – Balgen – Kraftprobe</span><br>Brazilian Jiu Jitsu zur Entwicklungsförderung</div>
    <div class="label" style="left:30px;top:228px"><span class="tag">Feste Schritte – Klarer Start</span><br>Kompetenztraining für einen gelingenden Schulstart</div>
  </div>
</section>

<section class="spread" style="left:139px;top:1006px">
  <div class="page left">
    <div class="bar" style="left:46px;top:20px">Toben – Balgen – Kraftprobe</div>
    <p class="para" style="left:76px;top:62px;width:210px">Das zentrale Ziel des Programms ist es, den Kindern wichtige Kompetenzen zu vermitteln, die notwendig sind, um friedlich und nach Anleitung miteinander kämpfen zu können. Dies stellt eine hohe emotionale Herausforderung dar und kann nur gelingen, wenn klare Regeln vereinbart und eingehalten werden. Um zu gewährleisten, dass das Training verletzungsfrei für alle teilnehmenden Kinder abläuft, teilen wir die Unterrichtsstunde in mehrere Phasen ein und nähern uns so dem freien Kämpfen Schritt für Schritt.</p>
    <div class="photo" role="img" aria-label="Foto: Kinder beim Tauziehen auf einer sonnigen Wiese" style="left:70px;top:154px;width:222px;height:166px;background:linear-gradient(120deg,#d9b48f,#8fb35c 45%,#5a8a3a)"></div>
  </div>
  <div class="page">
    <div class="bar small" style="left:28px;top:62px">Phase 1: Kennen lernen und Vertrauen aufbauen</div>
    <p class="para" style="left:30px;top:76px;width:236px">Der Prozess zum Aufbau eines vertrauensvollen Verhältnisses benötigt viel Zeit und pädagogisches Feingefühl. Je nachdem, wie gut sich Teilnehmer bereits untereinander kennen und wie stark die Heterogenität der Gruppe ausfällt, kann das Kennenlernen im Sitzkreis stattfinden oder durch einfache Spiele eine Vertrauensbasis geschaffen werden.</p>
    <div class="bar small" style="left:28px;top:140px">Phase 2: Erarbeiten der Regeln, Aufbau von Körperkon-<br>takt und allgemeines Aufwärmen</div>
    <p class="para" style="left:30px;top:164px;width:236px">Bereits zum Aufwärmen werden klare Regeln festgelegt. Dadurch soll den Teilnehmern verdeutlicht werden, wie wichtig die Einhaltung von Regeln allgemein und vor allem später beim Kämpfen ist. Wir nutzen verschiedene Spiele, um ersten Körperkontakt aufzubauen und um zu testen, inwieweit die Gruppe schon bereit für das Rangeln und Raufen ist. Bei jüngeren Kindern und Jugendlichen nutzen wir die Phase auch gerne um Geschicklichkeit und Kraft herauszufordern.</p>
  </div>
</section>

<section class="spread" style="left:423px;top:1432px">
  <div class="page left">
    <div class="bar small" style="left:48px;top:76px">Phase 3: Technikteil</div>
    <p class="para" style="left:50px;top:88px;width:232px">Einfache Basistechniken aus dem Brazilian Jiu Jitsu reichen aus, um den Gegenüber am Boden zu kontrollieren, ohne ihm dabei wehzutun. Die Kinder dürfen das Gezeigte partnerweise trainieren und ausprobieren. Dabei wird der Unterschied zwischen Miteinander und friedlichem Gegeneinander betont, damit ein Wir-Gefühl entsteht und die Kinder und Jugendlichen lernen zusammenzuarbeiten.</p>
    <div class="bar small" style="left:48px;top:164px">Phase 4: Rangel und Raufspiele</div>
    <p class="para" style="left:50px;top:176px;width:232px">Als Vorstufe zum freien Kämpfen dürfen die Teilnehmer nun erstmals vom Miteinander ins spielerische Gegeneinander übergehen. Wichtige Regeln werden nochmals wiederholt, bevor unter Anleitung verschiedene Positionen am Boden oder auch im Stand ausprobiert werden.</p>
    <div class="bar small" style="left:48px;top:230px">Phase 5: Freies Kämpfen</div>
    <p class="para" style="left:50px;top:242px;width:232px">Wenn deutlich wird, dass die Teilnehmer das Rangeln und Raufen in Phase 4 emotional gut verkraften, dürfen sie anschließend frei kämpfen. Das freie Kämpfen dient als Messlatte und zeigt, inwieweit die pädagogischen Ziele erreicht wurden.</p>
  </div>
  <div class="page">
    <ul class="checks" style="left:30px;top:76px;width:232px">
      <li>Übergriffige Kinder entwickeln eine kampfspezifische Fürsorge und achten auf die Gesundheit ihres Partners</li>
      <li>Unruhige Kinder lernen sich strategisch aus misslichen Lagen zu befreien</li>
      <li>Die Kinder erfahren unmittelbar, dass kritische Situationen und Konflikte durch ruhig durchdachte Strategien gelöst werden können</li>
      <li>Wenn Regeln verabredet werden, müssen sie eingehalten werden</li>
      <li>Durch das Rangeln und Raufen lernen die Kinder ihren Körper wahrzunehmen</li>
      <li>Die Kinder erhalten ein realistisches Selbstbild. Sie lernen, zu was sie im Stande sind</li>
    </ul>
    <div class="bar small" style="left:28px;top:228px">Phase 6: Auflockerung und Verarbeitung des Erlebten durch<br>Meditationsphase oder Abschlussspiel</div>
    <p class="para" style="left:30px;top:252px;width:232px">Ein Abschlussspiel ohne kämpferische Aspekte soll der Stunde einen Gegenpol bieten, um zum Miteinander zurückzufinden und ein spaßiges Ende für alle zu schaffen.</p>
  </div>
</section>

<section class="spread" style="left:131px;top:1855px">
  <div class="page left">
    <div class="bar" style="left:46px;top:34px">Feste Schritte – Klarer Start</div>
    <div class="photo" role="img" aria-label="Foto: Mädchen sitzt traurig zwischen Schulbänken im Klassenzimmer" style="left:68px;top:58px;width:216px;height:86px;background:linear-gradient(90deg,#3e6fa8,#d6d0c6 50%,#4b78b0)"></div>
    <div class="bar small" style="left:68px;top:208px">Wir stärken Kinder auf ihrem Weg ins Schulleben</div>
    <p class="para" style="left:70px;top:222px;width:216px">Selbstsicherheit und souveränes Auftreten sind die wichtigen Bausteine, nicht nur für einen gelingenden Schulstart, sondern auch für eine erfolgreiche Zukunft. Dabei ist es wichtig, Kinder auf Gefahren aufmerksam zu machen – ohne sie dabei zu verängstigen. Wir zeigen ihnen in unserem Kurs Mittel und Möglichkeiten, wie sie Belastungssituationen sicher und souverän bewältigen können.</p>
  </div>
  <div class="page">
    <div class="bar small" style="left:16px;top:30px">Die zentralen Themen unseres Kurses erstrecken sich dabei<br>über 4 Einheiten je 45 Minuten</div>
    <p class="para" style="left:18px;top:58px;width:224px"><span style="color:var(--red)">1.Einheit</span> | Wie gehe ich selbstsicher mit neuen Mitschülern um und wie finde ich neue Freunde?</p>
    <p class="para" style="left:18px;top:80px;width:224px"><span style="color:var(--red)">2.Einheit</span> | Wie verhalte ich mich souverän in Streitsituationen?</p>
    <p class="para" style="left:18px;top:96px;width:224px"><span style="color:var(--red)">3.Einheit</span> | Wie verhalte ich mich auf dem Schulweg und wie komme ich sicher nach Hause?</p>
    <p class="para" style="left:18px;top:120px;width:224px"><span style="color:var(--red)">4.Einheit</span> | Wie gehe ich mit Erfolgserlebnissen um und wie reagiere ich auf Rückschläge?</p>
    <div class="photo" role="img" aria-label="Foto: nachdenkliches Mädchen im Schulflur, dahinter spielende Kinder" style="left:18px;top:158px;width:208px;height:162px;background:linear-gradient(100deg,#e3d2b8,#9a7a62 45%,#4fa5b0)"></div>
  </div>
</section>

<section class="spread" style="left:428px;top:2282px">
  <div class="page left">
    <p class="para red" style="left:76px;top:24px;width:214px">Im Umgang mit Kindern im Vor- und Grundschulalter ist es besonders wichtig, die Inhalte spielerisch und anschaulich zu vermitteln. Die verbalen und körperlichen Strategien werden durch Rollenspiele geprobt und durch Inhalte der aktiven Selbstverteidigung ergänzt.</p>
    <p class="para red" style="left:76px;top:64px;width:214px">Speziell konzipierte Rangel- und Raufspiele unterstützen eine präventive Haltung der Inhalte und garantieren jede Menge Spaß und einen intensiven Lernprozess für alle teilnehmenden Kinder.</p>
    <div class="bar" style="left:46px;top:114px">Kursangebot</div>
    <div class="course" style="left:76px;top:140px;width:214px">
      <h3>Toben – Balgen – Kraftprobe</h3>
      <b>Kindergärten | Schulen | sonstige pädagogische Einrichtungen (Kinder- und Jugendheim etc.)</b>
      <p class="para">Gruppengröße und zeitlicher Rahmen des Kurses werden mit dem pädagogischen Personal vor Ort bestimmt. Schwerpunkte können in den Bereichen der Motorik und Gewaltprävention, im Antiaggressionstraining und der Jungenarbeit gesetzt werden.</p>
    </div>
    <div class="course" style="left:76px;top:240px;width:214px">
      <h3>Kompetenztraining – Feste Schritte – klarer Start</h3>
      <b>Kindergärten (4 x 45 min, max. 20 Teilnehmer)<br>Grundschulen bis einschließlich 5. Klasse<br>(4 x 45 min, 20–30 Teilnehmer)</b>
    </div>
  </div>
  <div class="page">
    <div class="photo" role="img" aria-label="Foto: Mädchen mit langen Haaren sitzt zusammengekauert an einer gefliesten Wand" style="left:18px;top:18px;width:262px;height:284px;background:linear-gradient(140deg,#c9c6c2,#a78a72 50%,#e0dcd6)"></div>
  </div>
</section>

<section class="spread" style="left:117px;top:2707px">
  <div class="page left">
    <div class="bar" style="left:50px;top:38px">Über uns</div>
    <div class="photo" role="img" aria-label="Foto: die beiden Trainer in schwarzen T-Shirts, Arm in Arm" style="left:100px;top:70px;width:176px;height:120px;background:linear-gradient(180deg,#f2f2f2,#d8c0a8 40%,#2a2a2a 70%)"></div>
    <div class="rule" style="left:48px;top:196px;width:259px"></div>
    <div class="person" style="left:56px;top:206px;width:112px"><strong>Jonas Rieder</strong>Bachelor of Arts Pädagogik/Sozialpädagogik, Hochschule Talheim<em>»Beim Rangeln entsteht Vertrauen, das Kinder auch im Alltag stärkt.«</em></div>
    <div class="person" style="left:196px;top:206px;width:104px"><strong>Lukas Brenner</strong>Bachelor of Arts Pädagogik, Hochschule Talheim<em>»Unser Anliegen ist es, Kindern den fairen Umgang mit Kraft zu zeigen.«</em></div>
  </div>
  <div class="page">
    <div class="bar" style="left:12px;top:32px">Lehrerstimmen</div>
    <div class="bar small" style="left:26px;top:70px">Wir legen viel Wert auf einen stetigen Austausch<br>mit den anwesenden Lehrkräften</div>
    <p class="para" style="left:30px;top:96px;width:236px"><strong>Merle Kranz (Mittelschule Lindenau)</strong><br>»Ich durfte den Kurs mit meiner Klasse begleiten. Die Kinder waren mit großer Freude dabei und haben gelernt, fair miteinander umzugehen.«</p>
    <p class="para" style="left:30px;top:140px;width:236px"><strong>Sandra Wolf (Grundschule Lindenau)</strong><br>»Besonders gefallen hat mir die ruhige Art der Trainer. Die Kinder konnten Kraft und Körperkontakt in sicheren Regeln erleben und haben viel über Fairness gelernt.«</p>
    <p class="para" style="left:30px;top:196px;width:236px"><strong>Ingrid Lauer | Carola Wendt (Mittelschule Lindenau)</strong><br>»Ein wertvolles Angebot für unsere Schüler. Durch kontrolliertes Kämpfen konnten sie Aggressionen abbauen und ihr Selbstvertrauen stärken. Die Klassengemeinschaft hat davon sehr profitiert.«</p>
  </div>
</section>

</body>
</html>
```